Business Card Design

I am a criminologist running a research and consultancy business on my own (PKConsultants)
I specialise in looking at fraud and other white-collar crimes. Also governance issues..
I would like a professional business card that would be appropriate both in the academic and business sector as I straddle both sectors. Normal shape - not square.
I am interested in seeing border Word Cloud type projects - black on white or white on black..
Example key words would be fraud, research, qualitative, interviews, quantitative, white-collar, reports, government, surveys, sample, governance, assurance, crime, offenders, prison etc (I can provide a full list if this is the option I go for). I also like Word Cloud borders as attached.
I am also interested in seeing other style business cards. Preferably one colour, plus black and white.
In particular I like black backgrounds with coloured words etc - colours like lime green are good.
I also like blues - especially teal if a traditional white background is chosen.
I don't have a logo - unless anyone can think of anything that's particularly appropriate.
Graphics can be used but they would be simple and stylish (dots, squares, lines, curves etc)
I would like the design to translate simply for a header for a website or blog.
My current website is www.pelling-hurst.com but is out of date in terms of what I do and design.
I have attached a number of things that have caught my eye and inspired me.
I have asked for a one-sided business card in the first instance - however if someone comes up with a good cloud design that might go on one side, I would consider a two-sided one.
Design can be landscape or portrait.
Kind Regards
Meg
Landscape
Contact Information for Business Card
PKConsultants
Dr Margery Pelling-Hurst, MSc, BSc, **
42 Brindle Wold
Callow, Brenmoorshire
KX27 4QD
+44(0)1620 482917
+44(0)7531 804152
www.pelling-hurst.com
margery@pelling-hurst.com

```html
<!DOCTYPE html>
<html lang="en">
<head>
<meta charset="utf-8">
<title>PKConsultants – Business Card</title>
<link href="https://fonts.googleapis.com/css2?family=Jost:wght@400;500&family=Oswald:wght@300;400&display=swap" rel="stylesheet">
<style>
  :root {
    --backdrop: #e4e4e4;
    --card-black: #121212;
    --card-white: #f4f4f4;
    --lime: #a4d45a;
    --text-white: #ffffff;
    --icon-white: #f0f0f0;
  }
  * { margin: 0; padding: 0; box-sizing: border-box; }
  html, body {
    width: 1200px; height: 720px; overflow: hidden;
    background: var(--backdrop);
  }
  .card {
    position: absolute; left: 180px; top: 120px;
    width: 840px; height: 480px;
    background: var(--card-black);
    overflow: hidden;
    box-shadow: 0 18px 40px rgba(0,0,0,0.22);
  }
  .card-shapes { position: absolute; inset: 0; }
  .brand {
    position: absolute; left: 200px; top: 38px;
    font-family: "Jost", sans-serif; font-weight: 500;
    font-size: 74px; letter-spacing: 1px; line-height: 1;
    color: var(--text-white);
  }
  .holder {
    position: absolute; left: 232px; top: 130px;
    font-family: "Oswald", sans-serif; font-weight: 300;
    font-size: 25px; letter-spacing: 0.3px;
    color: var(--text-white);
  }
  .contacts {
    position: absolute; left: 262px; top: 224px;
    font-family: "Oswald", sans-serif; font-weight: 300;
    font-size: 20px; color: var(--lime);
    display: flex; flex-direction: column; gap: 28px;
  }
  .contact-row { display: flex; gap: 22px; align-items: center; }
  .contact-item { display: flex; align-items: center; gap: 8px; white-space: nowrap; }
  .icon { width: 20px; height: 20px; flex: none; }
  .icon * { fill: none; stroke: var(--icon-white); stroke-width: 1.8; stroke-linecap: round; stroke-linejoin: round; }
</style>
</head>
<body>
  <div class="card">
    <svg class="card-shapes" viewBox="0 0 840 480" width="840" height="480" aria-hidden="true">
      <polygon class="white-wedge" points="0,0 96,0 240,178 28,480 0,480" fill="var(--card-white)"/>
      <polygon class="lime-band" points="120,0 840,0 840,178 262,178" fill="var(--lime)"/>
    </svg>

    <div class="brand">PKConsultants</div>
    <div class="holder">Dr Margery Pelling-Hurst, MSc, BSc</div>

    <div class="contacts">
      <div class="contact-row">
        <span class="contact-item">
          <svg class="icon" viewBox="0 0 20 20"><path d="M10 18s6-6 6-10.5a6 6 0 0 0-12 0C4 12 10 18 10 18z"/><circle cx="10" cy="7.5" r="2.2"/></svg>
          42 Brindle Wold Callow, Brenmoorshire KX27 4QD
        </span>
        <span class="contact-item">
          <svg class="icon" viewBox="0 0 20 20"><path d="M5 2.5l3 3.2-1.6 2.2a10 10 0 0 0 5.7 5.7l2.2-1.6 3.2 3-1.8 2.5C9.5 17 3 10.5 2.5 4.3z"/></svg>
          +44(0)7531 804152
        </span>
      </div>
      <div class="contact-row">
        <span class="contact-item">
          <svg class="icon" viewBox="0 0 20 20"><path d="M5 2.5l3 3.2-1.6 2.2a10 10 0 0 0 5.7 5.7l2.2-1.6 3.2 3-1.8 2.5C9.5 17 3 10.5 2.5 4.3z"/></svg>
          +44(0)1620 482917
        </span>
        <span class="contact-item">
          <svg class="icon" viewBox="0 0 20 20"><rect x="2.5" y="4.5" width="15" height="11"/><path d="M2.5 4.5l7.5 6.5 7.5-6.5"/></svg>
          margery@pelling-hurst.com
        </span>
      </div>
      <div class="contact-row">
        <span class="contact-item">
          <svg class="icon" viewBox="0 0 20 20"><circle cx="10" cy="10" r="3.2"/><path d="M13.2 7v4.2a2.3 2.3 0 0 0 4.5.3A8 8 0 1 0 14 17"/></svg>
          www.pelling-hurst.com
        </span>
      </div>
    </div>
  </div>
</body>
</html>
```